A resume/portfolio website for myself

I'm an independent software contractor, architect, tech trainer. I need a web site to present myself. Many ready to use portfolio designs are too artistic and focused on presenting design skills of the person. I like a nice website but the content should be a little less graphic than if you would present a graphic designer. Content could be presentation of me, core skill qualities and services and resume. Potentially a page with my tech courses in the longer run

```html
<!DOCTYPE html>
<html lang="en">
<head>
<meta charset="utf-8">
<title>Daniel Verhoef — Software Contractor</title>
<link href="https://fonts.googleapis.com/css2?family=Lato:ital,wght@0,400;0,700;0,900;1,400&display=swap" rel="stylesheet">
<style>
:root{
  --cyan:#00bff3;
  --teal:#15a3cc;
  --edu:#169bc3;
  --award:#19a8d3;
  --interest:#149fc8;
  --grey:#f2f2f2;
  --ink:#444;
  --muted:#8a8a8a;
  --dark:#0d7898;
  --field:#4dc2e2;
  --white:#fff;
}
*{box-sizing:border-box;margin:0;padding:0}
html,body{width:1200px;height:5106px;overflow:hidden}
body{font-family:'Lato',sans-serif;color:var(--ink);background:var(--white);position:relative}
section{position:relative;width:1200px;text-align:center}
.title{font-weight:900;font-size:25px;letter-spacing:1.5px;text-transform:uppercase;position:absolute;left:0;right:0}
.title::after{content:"";display:block;width:96px;height:4px;margin:12px auto 0;background:rgba(255,255,255,.45)}
.light .title{color:#444}
.light .title::after{background:#cfcfcf}
.dark .title{color:var(--white)}
.dark{color:var(--white)}

/* header */
.hero{height:502px;background:var(--grey)}
.hero-photo{position:absolute;left:0;top:0;width:1200px;height:252px;background:linear-gradient(100deg,#6b6663 0%,#8f8a85 45%,#5d5a58 100%)}
.hire{position:absolute;left:906px;top:14px;width:120px;height:42px;border:3px solid var(--cyan);border-radius:4px;background:#3d3b3a;color:#fff;font-weight:900;font-size:16px;line-height:36px;letter-spacing:1px}
.portrait{position:absolute;left:507px;top:145px;width:186px;height:186px;border-radius:50%;border:6px solid #fff;background:radial-gradient(circle at 50% 40%,#d9b79d 0%,#a9866e 45%,#6c8fb5 80%)}
.name{position:absolute;top:350px;left:0;right:0;font-size:28px;font-weight:700;color:#444;letter-spacing:.5px}
.meta{position:absolute;left:0;right:0;font-size:14px;color:var(--muted);letter-spacing:.6px}

/* about */
.about{height:273px;background:var(--cyan)}
.about p{position:absolute;left:170px;right:170px;top:108px;font-size:15px;line-height:24px}
.message{height:215px;background:var(--teal)}
.message blockquote{position:absolute;left:170px;right:170px;top:82px;font-size:19px;font-weight:900;line-height:30px}

/* timeline */
.work{height:781px;background:var(--grey)}
.edu{height:742px;background:var(--edu)}
.line{position:absolute;left:598px;width:2px;background:#cfcfcf}
.edu .line{background:rgba(255,255,255,.55)}
.tl{position:absolute;left:0;right:0;height:0}
.tl-dot{position:absolute;left:587px;top:-12px;width:24px;height:24px;border-radius:50%;background:var(--cyan);border:3px solid var(--grey)}
.edu .tl-dot{background:#fff;border-color:var(--edu)}
.tl-dot svg{display:block;margin:3px auto}
.tl-text{position:absolute;top:-56px;width:400px;font-size:12.5px;line-height:19px;color:#555}
.tl-text strong{display:block;font-size:17px;font-weight:900;letter-spacing:.5px;color:#444;line-height:20px}
.tl-text em{display:block;font-style:normal;font-size:11.5px;font-weight:900;letter-spacing:.5px;color:#444;margin-bottom:6px}
.edu .tl-text,.edu .tl-text strong,.edu .tl-text em{color:#fff}
.tl-left .tl-text{right:634px;text-align:right}
.tl-right .tl-text{left:634px;text-align:left}
.tl-date{position:absolute;top:-21px;width:182px;height:42px;border-radius:4px;background:var(--cyan);color:#fff;font-size:12.5px;font-weight:900;letter-spacing:1px;line-height:42px}
.tl-right .tl-date{left:640px}
.tl-left .tl-date{left:377px}
.tl-right .tl-date::before{content:"";position:absolute;left:-8px;top:13px;border:8px solid transparent;border-left:0;border-right-color:var(--cyan)}
.tl-left .tl-date::after{content:"";position:absolute;right:-8px;top:13px;border:8px solid transparent;border-right:0;border-left-color:var(--cyan)}

/* skills */
.skills{height:787px;background:var(--grey)}
.grid{position:absolute;left:160px;width:880px;display:grid;grid-template-columns:repeat(3,1fr);column-gap:0}
.skill h3{font-size:17px;font-weight:900;letter-spacing:.5px;color:#444;margin-bottom:10px}
.skill p{font-size:12.5px;line-height:24px;color:#777;padding:0 20px}
.divider{position:absolute;left:172px;right:172px;top:440px;height:1px;background:#d6d6d6}
.subtitle{position:absolute;top:463px;left:0;right:0;font-size:17px;font-weight:900;letter-spacing:1px;color:#444}
.refs{position:absolute;left:170px;width:860px;display:grid;grid-template-columns:1fr 1fr}
.ref h4{font-size:14px;font-weight:900;letter-spacing:.5px;color:#444}
.ref span{display:block;font-style:italic;font-size:13px;color:#888;margin:4px 0 2px}
.ref p{font-size:12px;font-weight:700;line-height:24px;color:#555;padding:0 20px}

/* social */
.social{height:258px;background:var(--cyan)}
.social-row{position:absolute;left:232px;width:736px;display:grid;grid-template-columns:repeat(8,92px)}
.social-row span{font-size:14px;font-weight:700;color:#fff;line-height:30px}
.social-row svg{display:block;margin:0 auto}

/* awards */
.awards{height:339px;background:var(--award)}
.award{position:absolute;width:270px;text-align:left;padding-left:46px}
.award i{position:absolute;left:0;top:0;width:36px;height:36px;border-radius:50%;background:#fff}
.award i svg{display:block;margin:8px auto}
.award h3{font-size:18px;font-weight:900;letter-spacing:.5px;line-height:20px}
.award p{font-size:15px;margin-top:8px}
.award small{display:block;font-size:11px;margin-top:10px;opacity:.9}

/* interests */
.interests{height:317px;background:var(--interest)}
.interests p{position:absolute;left:190px;right:190px;top:115px;font-size:13.5px;line-height:24px}
.hobby{position:absolute;top:184px;list-style:none;text-align:left}
.hobby li{font-size:13.5px;line-height:31px;padding-left:10px;border-left:2px solid rgba(255,255,255,.7);margin-bottom:0}

/* tweets */
.tweets{height:296px;background:var(--grey)}
.bird{position:absolute;left:175px;top:142px;width:90px;text-align:center}
.bird i{display:block;width:50px;height:50px;margin:0 auto 6px;border-radius:50%;background:var(--cyan)}
.bird span{font-size:15px;font-weight:900;color:var(--cyan)}
.tweet{position:absolute;left:297px;top:113px;width:716px;height:145px;background:#fff;border-radius:6px;text-align:left;padding:18px 22px;font-size:12.5px;line-height:17px;font-weight:700;color:#444}
.tweet::before{content:"";position:absolute;left:-12px;top:56px;border:12px solid transparent;border-left:0;border-right-color:#fff}
.tweet a{color:var(--cyan);text-decoration:none}
.tweet small{position:absolute;left:22px;bottom:14px;font-size:11px;font-weight:400;color:#999}

/* contact */
.contact{height:521px;background:var(--award)}
.field{position:absolute;background:var(--field);border-radius:4px;color:#fff;font-size:14px;font-weight:900;letter-spacing:1px;text-align:left;padding:12px 14px}
.captcha{position:absolute;left:264px;top:408px;width:327px;height:40px;background:#f4f4f4;border-radius:3px;color:var(--teal);font-weight:900;font-size:14px;letter-spacing:1px;line-height:40px}
.captcha-in{position:absolute;left:617px;top:408px;width:325px;height:40px;background:var(--field);border-radius:3px}
.submit{position:absolute;left:262px;top:470px;width:680px;height:51px;background:var(--dark);border-radius:5px;color:#fff;font-weight:900;font-size:21px;letter-spacing:1.5px;line-height:51px}
footer{height:75px;background:#fff;text-align:center;font-size:12.5px;font-weight:700;color:#555;padding-top:49px}
</style>
</head>
<body>

<section class="hero">
  <div class="hero-photo" role="img" aria-label="Blurred photo of a desk with a laptop"></div>
  <div class="hire">HIRE ME &gt;</div>
  <div class="portrait" role="img" aria-label="Portrait photo of Daniel Verhoef"></div>
  <h1 class="name">DANIEL VERHOEF</h1>
  <p class="meta" style="top:390px">software contractor, architect, tech trainer</p>
  <p class="meta" style="top:412px">London, United Kingdom &nbsp;software Services</p>
  <p class="meta" style="top:435px">useremail@domain.com</p>
</section>

<section class="about dark">
  <h2 class="title" style="top:40px">About me</h2>
  <p>Lorem ipsum dolor sit amet, consectetur adipiscing elit. Pellentesque at arcu tincidunt, condimentum neque vitae, lacinia quam. <strong>Sed eu enim</strong> eget ligula dictum gravida. Pellentesque lacinia eleifend lectus, vel bibendum urna scelerisque id. Aliquam ac elit euismod, blandit arcu non, consectetur diam. Aliquam at sem congue, malesuada arcu non, blandit augue. Vestibulum ac magna erat. Interdum et malesuada fames ac ante ipsum primis in faucibus. Nunc dapibus metus eros.</p>
</section>

<section class="message dark">
  <h2 class="title" style="top:33px">Daily message</h2>
  <blockquote>“Lorem ipsum dolor sit amet, consectetur adipiscing elit. Pellentesque at arcu tincidunt, condimentum neque vitae, lacinia quam. Sed eu enim eget ligula dictum gravida.”</blockquote>
</section>

<section class="work light">
  <h2 class="title" style="top:33px">Work experience</h2>
  <div class="line" style="top:100px;height:650px"></div>

  <div class="tl tl-left" style="top:164px">
    <div class="tl-text"><strong>COMPANY</strong><em>JOB TITLE</em>Lorem ipsum dolor sit amet, consectetur adipiscing elit. In a eleifend risus, vel vehicula enim. Pellentesque lobortis vulputate tellus, quis facilisis sapien.</div>
    <div class="tl-dot"><svg width="12" height="12" viewBox="0 0 12 12"><rect x="1" y="4" width="10" height="7" rx="1" fill="#fff"/><rect x="4" y="2" width="4" height="3" fill="none" stroke="#fff" stroke-width="1.2"/></svg></div>
    <div class="tl-date" style="left:640px">JUNE 12 - CURRENT</div>
  </div>
  <div class="tl tl-right" style="top:335px">
    <div class="tl-date" style="left:377px">DEC 11- JULY 12</div>
    <div class="tl-dot"><svg width="12" height="12" viewBox="0 0 12 12"><rect x="1" y="4" width="10" height="7" rx="1" fill="#fff"/><rect x="4" y="2" width="4" height="3" fill="none" stroke="#fff" stroke-width="1.2"/></svg></div>
    <div class="tl-text"><strong>COMPANY</strong><em>JOB TITLE</em>Lorem ipsum dolor sit amet, consectetur adipiscing elit. In a eleifend risus, vel vehicula enim. Pellentesque lobortis vulputate tellus, quis facilisis sapien.</div>
  </div>
  <div class="tl tl-left" style="top:499px">
    <div class="tl-text"><strong>COMPANY</strong><em>JOB TITLE</em>Lorem ipsum dolor sit amet, consectetur adipiscing elit. In a eleifend risus, vel vehicula enim. Pellentesque lobortis vulputate tellus, quis facilisis sapien.</div>
    <div class="tl-dot"><svg width="12" height="12" viewBox="0 0 12 12"><rect x="1" y="4" width="10" height="7" rx="1" fill="#fff"/><rect x="4" y="2" width="4" height="3" fill="none" stroke="#fff" stroke-width="1.2"/></svg></div>
    <div class="tl-date" style="left:640px">APRIL 11 - DEC 11</div>
  </div>
  <div class="tl tl-right" style="top:668px">
    <div class="tl-date" style="left:377px">JAN 10 - APRIL 11</div>
    <div class="tl-dot"><svg width="12" height="12" viewBox="0 0 12 12"><rect x="1" y="4" width="10" height="7" rx="1" fill="#fff"/><rect x="4" y="2" width="4" height="3" fill="none" stroke="#fff" stroke-width="1.2"/></svg></div>
    <div class="tl-text"><strong>COMPANY</strong><em>JOB TITLE</em>Lorem ipsum dolor sit amet, consectetur adipiscing elit. In a eleifend risus, vel vehicula enim. Pellentesque lobortis vulputate tellus, quis facilisis sapien.</div>
  </div>
</section>

<section class="edu dark">
  <h2 class="title" style="top:42px">Education</h2>
  <div class="line" style="top:110px;height:610px"></div>

  <div class="tl tl-left" style="top:174px">
    <div class="tl-text"><strong>DEGREE</strong><em>UNIVERSITY</em>Lorem ipsum dolor sit amet, consectetur adipiscing elit. In a eleifend risus, vel vehicula enim. Pellentesque lobortis vulputate tellus, quis facilisis sapien.</div>
    <div class="tl-dot"><svg width="12" height="12" viewBox="0 0 12 12"><path d="M6 2 L12 5 L6 8 L0 5Z" fill="#169bc3"/><path d="M3 6.5 V9 Q6 11 9 9 V6.5" fill="#169bc3"/></svg></div>
    <div class="tl-date" style="left:640px">JUNE 12 - CURRENT</div>
  </div>
  <div class="tl tl-right" style="top:343px">
    <div class="tl-date" style="left:377px">DEC 11- JULY 12</div>
    <div class="tl-dot"><svg width="12" height="12" viewBox="0 0 12 12"><path d="M6 2 L12 5 L6 8 L0 5Z" fill="#169bc3"/><path d="M3 6.5 V9 Q6 11 9 9 V6.5" fill="#169bc3"/></svg></div>
    <div class="tl-text"><strong>DEGREE</strong><em>UNIVERSITY</em>Lorem ipsum dolor sit amet, consectetur adipiscing elit. In a eleifend risus, vel vehicula enim. Pellentesque lobortis vulputate tellus, quis facilisis sapien.</div>
  </div>
  <div class="tl tl-left" style="top:500px">
    <div class="tl-text"><strong>DEGREE</strong><em>UNIVERSITY</em>Lorem ipsum dolor sit amet, consectetur adipiscing elit. In a eleifend risus, vel vehicula enim. Pellentesque lobortis vulputate tellus, quis facilisis sapien.</div>
    <div class="tl-dot"><svg width="12" height="12" viewBox="0 0 12 12"><path d="M6 2 L12 5 L6 8 L0 5Z" fill="#169bc3"/><path d="M3 6.5 V9 Q6 11 9 9 V6.5" fill="#169bc3"/></svg></div>
    <div class="tl-date" style="left:640px">APRIL 11 - DEC 11</div>
  </div>
  <div class="tl tl-right" style="top:670px">
    <div class="tl-date" style="left:377px">JAN 10 - APRIL 11</div>
    <div class="tl-dot"><svg width="12" height="12" viewBox="0 0 12 12"><path d="M6 2 L12 5 L6 8 L0 5Z" fill="#169bc3"/><path d="M3 6.5 V9 Q6 11 9 9 V6.5" fill="#169bc3"/></svg></div>
    <div class="tl-text"><strong>DEGREE</strong><em>UNIVERSITY</em>Lorem ipsum dolor sit amet, consectetur adipiscing elit. In a eleifend risus, vel vehicula enim. Pellentesque lobortis vulputate tellus, quis facilisis sapien.</div>
  </div>
</section>

<section class="skills light">
  <h2 class="title" style="top:95px">Technical skills</h2>
  <div class="grid" style="top:162px">
    <div class="skill"><h3>LOREM IPSUM</h3><p>Lorem ipsum dolor sit amet, consectetur adipiscing elit. Pellentesque at arcu tincidunt, condimentum neque quam.</p></div>
    <div class="skill"><h3>LOREM IPSUM</h3><p>Lorem ipsum dolor sit amet, consectetur adipiscing elit. Pellentesque at arcu tincidunt, condimentum neque quam.</p></div>
    <div class="skill"><h3>LOREM IPSUM</h3><p>Lorem ipsum dolor sit amet, consectetur adipiscing elit. Pellentesque at arcu tincidunt, condimentum neque quam.</p></div>
  </div>
  <div class="grid" style="top:299px">
    <div class="skill"><h3>LOREM IPSUM</h3><p>Lorem ipsum dolor sit amet, consectetur adipiscing elit. Pellentesque at arcu tincidunt, condimentum neque quam.</p></div>
    <div class="skill"><h3>LOREM IPSUM</h3><p>Lorem ipsum dolor sit amet, consectetur adipiscing elit. Pellentesque at arcu tincidunt, condimentum neque quam.</p></div>
    <div class="skill"><h3>LOREM IPSUM</h3><p>Lorem ipsum dolor sit amet, consectetur adipiscing elit. Pellentesque at arcu tincidunt, condimentum neque quam.</p></div>
  </div>
  <div class="divider"></div>
  <h3 class="subtitle">REFERENCES</h3>
  <div class="refs" style="top:510px">
    <div class="ref"><h4>JOHN DOE</h4><span>Job Title Goes Here</span><p>“Lorem ipsum dolor sit amet, consectetur adipiscing elit. Pellentesque at arcu tincidunt, condimentum neque quam.”</p></div>
    <div class="ref"><h4>JOHN DOE</h4><span>Job Title Goes Here</span><p>“Lorem ipsum dolor sit amet, consectetur adipiscing elit. Pellentesque at arcu tincidunt, condimentum neque quam.”</p></div>
  </div>
  <div class="refs" style="top:655px">
    <div class="ref"><h4>JOHN DOE</h4><span>Job Title Goes Here</span><p>“Lorem ipsum dolor sit amet, consectetur adipiscing elit. Pellentesque at arcu tincidunt, condimentum neque quam.”</p></div>
    <div class="ref"><h4>JOHN DOE</h4><span>Job Title Goes Here</span><p>“Lorem ipsum dolor sit amet, consectetur adipiscing elit. Pellentesque at arcu tincidunt, condimentum neque quam.”</p></div>
  </div>
</section>

<section class="social dark">
  <h2 class="title" style="top:25px">Check my social connections</h2>
  <div class="social-row" style="top:106px">
    <span>Clipstream</span><span>Worklink</span><span>Chirper</span><span>Snapframe</span><span>Vimora</span><span>Codecat</span><span>Stackly</span><span>Dribbo</span>
  </div>
  <div class="social-row" style="top:188px">
    <span>Spotcheck</span><span>Tunelog</span><span>Callbox</span>
    <span><svg width="30" height="30" viewBox="0 0 30 30"><circle cx="7" cy="23" r="3.5" fill="#fff"/><path d="M4 13 A13 13 0 0 1 17 26" fill="none" stroke="#fff" stroke-width="3.5"/><path d="M4 5 A21 21 0 0 1 25 26" fill="none" stroke="#fff" stroke-width="3.5"/></svg></span>
    <span><svg width="30" height="34" viewBox="0 0 30 34"><rect x="7" y="2" width="16" height="30" rx="2" fill="none" stroke="#fff" stroke-width="2"/><line x1="7" y1="7" x2="23" y2="7" stroke="#fff" stroke-width="1.5"/><line x1="7" y1="26" x2="23" y2="26" stroke="#fff" stroke-width="1.5"/></svg></span>
    <span>Friendly</span>
    <span><svg width="34" height="34" viewBox="0 0 34 34" fill="none" stroke="#fff" stroke-width="2"><circle cx="17" cy="17" r="14"/><ellipse cx="17" cy="17" rx="6" ry="14"/><line x1="3" y1="17" x2="31" y2="17"/><line x1="6" y1="10" x2="28" y2="10"/><line x1="6" y1="24" x2="28" y2="24"/></svg></span>
    <span>Inkpost</span>
  </div>
</section>

<section class="awards dark">
  <h2 class="title" style="top:43px">Awards &amp; achievements</h2>
  <div class="award" style="left:174px;top:130px"><i><svg width="20" height="20" viewBox="0 0 20 20"><circle cx="10" cy="8" r="6" fill="#19a8d3"/><path d="M7 13 L6 19 L10 17 L14 19 L13 13Z" fill="#19a8d3"/></svg></i><h3>LOREM IPSUM</h3><p>Lorem ipsum dolor sit amet</p><small>Received: &nbsp;June, 22nd 2014</small></div>
  <div class="award" style="left:464px;top:130px"><i><svg width="20" height="20" viewBox="0 0 20 20"><circle cx="10" cy="8" r="6" fill="#19a8d3"/><path d="M7 13 L6 19 L10 17 L14 19 L13 13Z" fill="#19a8d3"/></svg></i><h3>LOREM IPSUM</h3><p>Lorem ipsum dolor sit amet</p><small>Received: &nbsp;June, 22nd 2014</small></div>
  <div class="award" style="left:755px;top:130px"><i><svg width="20" height="20" viewBox="0 0 20 20"><circle cx="10" cy="8" r="6" fill="#19a8d3"/><path d="M7 13 L6 19 L10 17 L14 19 L13 13Z" fill="#19a8d3"/></svg></i><h3>LOREM IPSUM</h3><p>Lorem ipsum dolor sit amet</p><small>Received: &nbsp;June, 22nd 2014</small></div>
  <div class="award" style="left:174px;top:238px"><i><svg width="20" height="20" viewBox="0 0 20 20"><circle cx="10" cy="8" r="6" fill="#19a8d3"/><path d="M7 13 L6 19 L10 17 L14 19 L13 13Z" fill="#19a8d3"/></svg></i><h3>LOREM IPSUM</h3><p>Lorem ipsum dolor sit amet</p><small>Received: &nbsp;June, 22nd 2014</small></div>
  <div class="award" style="left:464px;top:238px"><i><svg width="20" height="20" viewBox="0 0 20 20"><circle cx="10" cy="8" r="6" fill="#19a8d3"/><path d="M7 13 L6 19 L10 17 L14 19 L13 13Z" fill="#19a8d3"/></svg></i><h3>LOREM IPSUM</h3><p>Lorem ipsum dolor sit amet</p><small>Received: &nbsp;June, 22nd 2014</small></div>
  <div class="award" style="left:755px;top:238px"><i><svg width="20" height="20" viewBox="0 0 20 20"><circle cx="10" cy="8" r="6" fill="#19a8d3"/><path d="M7 13 L6 19 L10 17 L14 19 L13 13Z" fill="#19a8d3"/></svg></i><h3>LOREM IPSUM</h3><p>Lorem ipsum dolor sit amet</p><small>Received: &nbsp;June, 22nd 2014</small></div>
</section>

<section class="interests dark">
  <h2 class="title" style="top:42px">Interests &amp; hobbies</h2>
  <p>Lorem ipsum dolor sit amet, consectetur adipiscing elit. Nunc vitae dapibus turpis, eu rutrum justo. Donec pellentesque pellentesque felis, vitae semper nisi vehicula semper. Nam nibh orci, <strong>semper sed</strong> dolor quis, semper convallis mi.</p>
  <ul class="hobby" style="left:365px"><li>Lorem ipsum dolor</li><li>Sit amet consectetuer</li><li>Elit sed</li><li>Diam nonummy nibh</li></ul>
  <ul class="hobby" style="left:664px"><li>Lorem ipsum dolor</li><li>Sit amet consectetuer</li><li>Elit sed</li><li>Diam nonummy nibh</li></ul>
</section>

<section class="tweets light">
  <h2 class="title" style="top:43px">Latest tweets</h2>
  <div class="bird"><i></i><span>Chirper</span></div>
  <div class="tweet"><a>@lenaparker</a> Lorem ipsum dolor sit amet, consectetur adipiscing elit. Vestibulum justo leo, aliquam id sagittis sit amet, consequat non elit. Etiam laoreet gravida sapien, vel ornare purus malesuada sit amet. Donec pellentesque tincidunt augue, quis tempus lectus cursus sed. Aenean vel imperdiet dolor. Mauris dapibus sodales orci non consequat.<small>about a day ago</small></div>
</section>

<section class="contact dark">
  <h2 class="title" style="top:40px">Let's get in touch</h2>
  <div class="field" style="left:260px;top:108px;width:327px;height:40px;padding-top:11px">YOUR NAME</div>
  <div class="field" style="left:615px;top:108px;width:323px;height:40px;padding-top:11px">YOUR EMAIL</div>
  <div class="field" style="left:260px;top:170px;width:678px;height:212px">YOUR MESSAGE</div>
  <div class="captcha">CAPTCHA</div>
  <div class="captcha-in"></div>
  <div class="submit">SUBMIT</div>
</section>

<footer>© 2020 Daniel Verhoef. All Rights Reserved.</footer>

</body>
</html>
```